Client Proposal

I need a proposal template to give to potential clients detailing our services, safety, company history, table of contents and appendixes. I need a cover page to start with images describing our services. Our company is based in Grande Prairie, Alberta. We do land survey work, engineering and environmental.

In word format please so that we can change the proposal on an as needed basis.

```html
<!DOCTYPE html>
<html lang="en">
<head>
<meta charset="utf-8">
<title>Proposal Cover – Meridian Group</title>
<link href="https://fonts.googleapis.com/css2?family=League+Spartan:wght@700&family=Jost:wght@600&family=Roboto:wght@400&display=swap" rel="stylesheet">
<style>
  :root {
    --brand-blue: #1394ce;
    --brand-gray: #85878a;
    --body-gray: #7a7d80;
    --paper: #ffffff;
    --backdrop: #ebeced;
    --photo-light: #b9bcbf;
    --photo-dark: #3e4043;
  }
  * { margin: 0; padding: 0; box-sizing: border-box; }
  html, body { width: 1200px; height: 1200px; overflow: hidden; }
  body { background: var(--backdrop); position: relative; font-family: "Roboto", Arial, sans-serif; }

  .cover {
    position: absolute; left: 171px; top: 30px;
    width: 858px; height: 1140px;
    background: var(--paper);
    overflow: hidden;
  }
  .cover-shapes { position: absolute; inset: 0; width: 100%; height: 100%; }

  .headline {
    position: absolute; left: 88px; top: 66px;
    font-family: "League Spartan", "Arial Black", sans-serif;
    font-weight: 700; font-size: 88px; line-height: 1; letter-spacing: -1px;
    color: var(--brand-gray);
  }
  .headline .accent { color: var(--brand-blue); }
  .subheadline {
    position: absolute; left: 92px; top: 143px;
    font-size: 35px; line-height: 1; letter-spacing: 0.5px;
    color: var(--brand-blue);
  }
  .intro, .summary {
    position: absolute; left: 87px;
    font-size: 13px; line-height: 17px; color: var(--body-gray);
  }
  .intro { top: 196px; }
  .summary { top: 1052px; }

  .brand-mark {
    position: absolute; left: 660px; top: 76px; width: 140px;
    display: flex; flex-direction: column; align-items: center; gap: 12px;
  }
  .brand-mark .square { width: 58px; height: 58px; background: var(--brand-blue); }
  .brand-mark .name {
    font-family: "Roboto", Arial, sans-serif; font-weight: 400;
    font-size: 20px; line-height: 1.1; text-align: center; letter-spacing: 1px;
    color: var(--brand-blue);
  }

  .company {
    position: absolute; left: 87px; top: 970px;
    font-family: "Jost", Arial, sans-serif; font-weight: 600;
    font-size: 37px; line-height: 1; color: var(--brand-gray);
  }
  .company .accent { color: var(--brand-blue); }
  .contact-person {
    position: absolute; left: 87px; top: 1016px;
    font-size: 20px; line-height: 1; color: var(--brand-blue);
  }

  .contact-list {
    position: absolute; left: 624px; top: 982px;
    list-style: none; display: flex; flex-direction: column; gap: 11px;
  }
  .contact-list li {
    display: flex; align-items: center; gap: 7px;
    font-size: 15.5px; line-height: 20px; color: var(--brand-blue); letter-spacing: 0.3px;
  }
  .contact-list svg { width: 22px; height: 22px; flex: none; }
</style>
</head>
<body>
  <main class="cover">
    <svg class="cover-shapes" viewBox="0 0 1173 1560" preserveAspectRatio="none">
      <defs>
        <linearGradient id="photo-tone" x1="0" y1="0" x2="1" y2="1">
          <stop offset="0" stop-color="var(--photo-light)"/>
          <stop offset="0.55" stop-color="#7d8084"/>
          <stop offset="1" stop-color="var(--photo-dark)"/>
        </linearGradient>
      </defs>
      <polygon class="hero-photo" role="img"
               aria-label="Black and white photograph of a large excavator on a cleared work site under a cloudy sky"
               points="0,371 1173,371 1173,776 587,936 0,776" fill="url(#photo-tone)"/>
      <polygon class="hero-band" points="0,814 587,974 1173,814 1173,1311 587,1157 0,1311" fill="var(--brand-blue)"/>
    </svg>

    <h1 class="headline"><span class="accent">HEAD</span>LINE</h1>
    <p class="subheadline">YOUR SUB HEADLINE</p>
    <p class="intro">Lorem ipsum dolor sit amet, consectetur adipiscing elit. Fusce leo augue,<br>laoreet ut rhoncus nec, faucibus quis lectus</p>

    <div class="brand-mark">
      <span class="square"></span>
      <span class="name">MERIDIAN<br>GROUP</span>
    </div>

    <h2 class="company"><span class="accent">Meridian</span> Group</h2>
    <p class="contact-person">President Dana Whitford</p>
    <p class="summary">Lorem ipsum dolor sit amet, consectetur adipiscing elit.<br>laoreet ut rhoncus nec, faucibus quis lectus</p>

    <ul class="contact-list">
      <li>
        <svg viewBox="0 0 24 24" fill="none" stroke="var(--brand-blue)" stroke-width="1.6">
          <circle cx="12" cy="12" r="10.5"/>
          <path d="M8.5 6.8l1.8-.4 1.1 2.6-1.2 1c.6 1.5 1.7 2.6 3.2 3.2l1-1.2 2.6 1.1-.4 1.8c-4.4.4-8.5-3.7-8.1-8.1z" fill="var(--brand-blue)" stroke-linejoin="round"/>
        </svg>
        780-555-0142
      </li>
      <li>
        <svg viewBox="0 0 24 24" fill="none" stroke="var(--brand-blue)" stroke-width="1.6">
          <rect x="2" y="5.5" width="20" height="13" rx="1"/>
          <path d="M2.5 6l9.5 7.5L21.5 6M2.5 18l7-6M21.5 18l-7-6"/>
        </svg>
        dana@meridiangroup.ca
      </li>
      <li>
        <svg viewBox="0 0 24 24" fill="none" stroke="var(--brand-blue)" stroke-width="1.4">
          <circle cx="12" cy="12" r="10"/>
          <ellipse cx="12" cy="12" rx="4.5" ry="10"/>
          <path d="M2 12h20M4 6.5h16M4 17.5h16M12 2v20"/>
        </svg>
        www.meridiangroup.ca
      </li>
    </ul>
  </main>
</body>
</html>
```